Copperleaf Motorized Shade Business Card

Hello, we've had our logo made. Now we are looking for a clean and cool looking business card. One side can just be the logo with any design elements that might look good with it. The other side will be Name, Phone Number and Email. There will not be an address on the card.

```html
<!DOCTYPE html>
<html lang="en">
<head>
<meta charset="utf-8">
<title>Copperleaf Motorized Shade – Business Card</title>
<link href="https://fonts.googleapis.com/css2?family=Bebas+Neue&family=League+Spartan:wght@500&display=swap" rel="stylesheet">
<style>
  :root {
    --page-bg: #ececea;
    --card-bg: #f7f7f5;
    --navy: #0f2a5c;
    --ink: #15120c;
    --sun-yellow: #f4b811;
    --sun-orange: #ee8a0c;
    --sun-red: #e2501b;
  }
  html, body {
    margin: 0;
    padding: 0;
    overflow: hidden;
  }
  body {
    width: 1026px;
    height: 1200px;
    background: var(--page-bg);
    position: relative;
  }
  .card {
    position: absolute;
    left: 153px;
    width: 720px;
    height: 412px;
    background: var(--card-bg);
    box-shadow: 0 18px 40px rgba(0,0,0,0.18);
    overflow: hidden;
  }
  .card--front { top: 146px; }
  .card--back  { top: 643px; }
  .card__art {
    position: absolute;
    inset: 0;
    width: 100%;
    height: 100%;
  }
  .decor-area {
    position: absolute;
    top: 0;
    right: 0;
    width: 250px;
    height: 100%;
    background: linear-gradient(200deg, var(--sun-orange) 0%, var(--sun-yellow) 100%);
  }
  .brand-name {
    position: absolute;
    left: 38px;
    top: 252px;
    margin: 0;
    font-family: "Bebas Neue", "Oswald", sans-serif;
    font-weight: 400;
    color: var(--navy);
    line-height: 1;
  }
  .brand-name__main {
    display: block;
    font-size: 86px;
    letter-spacing: 1px;
  }
  .brand-name__sub {
    display: block;
    margin-top: 6px;
    font-size: 20px;
    letter-spacing: 13px;
  }
  .contact {
    position: absolute;
    left: 69px;
    top: 236px;
    color: var(--ink);
  }
  .contact__name {
    margin: 0 0 12px;
    font-family: "Bebas Neue", "Oswald", sans-serif;
    font-weight: 400;
    font-size: 54px;
    letter-spacing: 2.5px;
    line-height: 1;
  }
  .contact__line {
    margin: 0;
    font-family: "League Spartan", "Helvetica", sans-serif;
    font-weight: 500;
    font-size: 24px;
    line-height: 32px;
  }
</style>
</head>
<body>

  <section class="card card--front" aria-label="Card front">
    <div class="decor-area" role="img" aria-label="Decorative orange sun graphic"></div>
    <h1 class="brand-name">
      <span class="brand-name__main">Copperleaf</span>
      <span class="brand-name__sub">Motorized Shade</span>
    </h1>
  </section>

  <section class="card card--back" aria-label="Card back">
    <svg class="card__art" viewBox="0 0 912 522" preserveAspectRatio="none" aria-hidden="true">
      <defs>
        <linearGradient id="band" x1="0" y1="0" x2="1" y2="0">
          <stop offset="0" stop-color="var(--sun-yellow)"/>
          <stop offset="0.55" stop-color="var(--sun-orange)"/>
          <stop offset="1" stop-color="var(--sun-red)"/>
        </linearGradient>
        <linearGradient id="panel" x1="0" y1="0" x2="1" y2="0">
          <stop offset="0" stop-color="var(--sun-yellow)"/>
          <stop offset="0.6" stop-color="#f2a40f"/>
          <stop offset="1" stop-color="#e8671a"/>
        </linearGradient>
      </defs>
      <rect class="top-band" x="33" y="32" width="842" height="73" rx="36" fill="url(#band)"/>
      <path class="info-panel" fill="url(#panel)"
        d="M58,148 L850,246 Q875,249 875,274 L875,462 Q875,487 850,487 L58,487 Q33,487 33,462 L33,172 Q33,145 58,148 Z"/>
    </svg>
    <div class="contact">
      <h2 class="contact__name">Firstname Lastname</h2>
      <p class="contact__line">firstname@domainname.com</p>
      <p class="contact__line">+1 234 687 982</p>
    </div>
  </section>

</body>
</html>
```